Trucking/service truck *Updated

Cards for a trucking company. Company transfers logs to saw mills. We are looking for something edgy, modern and fun. It's very limited when it comes to trucking business card choices. Plus the owner also runs an on-site service truck. He has 20+ years mechanic experience.
Colors are open. Favorites are orange & purple, but not must have. We really want to emphasize trust, dependability and knowledge with a bright, attention getter.
On card:
Hallowell & Hallowell
Dean Hallowell - Owner/Manager/Maintenance 903-512-4097
Marla Hallowell -Office Administration/Bookkeeping 903-627-1954
4718 Juniper Ln.
Larkfield, Ohio 75392
903-659-3021 - Office
Updates
Just a thought. Do you think you can combine the Taurus and Pisces signs? And put in the corner, or on the back or anything really? Thanks! You all or doing fantastic!
Industry/Entity Type
Business
Colors
Designer to choose colors to be used in the design.
Look and feel
Each slider illustrates characteristics of the customer's brand and the style your logo design should communicate.

```html
<!DOCTYPE html>
<html lang="en">
<head>
<meta charset="utf-8">
<title>Hallowell &amp; Hallowell — Business Cards</title>
<link rel="stylesheet" href="https://fonts.googleapis.com/css2?family=Roboto+Slab:wght@300;400;700&display=swap">
<style>
  :root {
    --backdrop: #dcdcdc;
    --paper: #fbfbfb;
    --navy: #0f2f52;
    --accent-blue: #1f6aa5;
    --ink: #13294a;
    --light-text: #e9eef5;
    --photo-forest: #6b7458;
    --photo-road: #a68a6a;
    --photo-truck: #3a3d42;
  }
  * { margin: 0; padding: 0; box-sizing: border-box; }
  html, body {
    width: 1200px; height: 1011px; overflow: hidden;
    background: var(--backdrop);
  }
  .card-sheet {
    position: absolute; top: 0; left: 0;
    width: 1200px; height: 1011px;
    display: block;
  }
  .card-shadow { fill: rgba(0,0,0,0.12); }
  .card-paper { fill: var(--paper); }
  .brand-name { font-family: "Roboto Slab", serif; font-weight: 400; fill: var(--ink); }
  .back-brand { font-family: "Roboto Slab", serif; font-weight: 300; fill: var(--light-text); letter-spacing: 0.5px; }
  .person-name { font-family: "Roboto Slab", serif; font-weight: 700; fill: #ffffff; letter-spacing: 0.5px; }
  .person-role { font-family: "Roboto Slab", serif; font-weight: 300; fill: #ffffff; }
  .contact-light { font-family: "Roboto Slab", serif; font-weight: 700; fill: #ffffff; }
  .contact-dark { font-family: "Roboto Slab", serif; font-weight: 400; fill: var(--ink); }
  .arc-rule { fill: none; stroke: var(--accent-blue); stroke-width: 2.5; }
  .icon-dark { fill: var(--accent-blue); }
  .icon-light { fill: #ffffff; }
</style>
</head>
<body>
<svg class="card-sheet" viewBox="0 0 1200 1011" xmlns="http://www.w3.org/2000/svg">
  <defs>
    <linearGradient id="photo-tones" x1="0" y1="0" x2="0" y2="1">
      <stop offset="0" stop-color="var(--photo-forest)"/>
      <stop offset="0.45" stop-color="var(--photo-truck)"/>
      <stop offset="0.75" stop-color="#7d6a52"/>
      <stop offset="1" stop-color="var(--photo-road)"/>
    </linearGradient>
    <clipPath id="front-clip"><rect width="400" height="700" rx="4"/></clipPath>
    <clipPath id="back-clip"><rect width="400" height="700" rx="4"/></clipPath>
  </defs>

  <g class="card card-front" transform="translate(150 155)">
    <rect class="card-shadow" x="6" y="8" width="400" height="700" rx="4"/>
    <g clip-path="url(#front-clip)">
      <rect class="card-paper" width="400" height="700"/>
      <rect class="truck-photo" width="400" height="700" fill="url(#photo-tones)"
            role="img" aria-label="Photo of a logging truck loaded with logs on a forest dirt road"/>
      <path class="card-paper" d="M0,0 H400 V150 C330,285 90,300 0,235 Z"/>
      <path class="arc-rule" d="M400,150 C330,285 90,300 0,235"/>
      <text class="brand-name" x="200" y="140" font-size="28" text-anchor="middle">Hallowell &amp; Hallowell</text>
    </g>
  </g>

  <g class="card card-back" transform="translate(650 155)">
    <rect class="card-shadow" x="6" y="8" width="400" height="700" rx="4"/>
    <g clip-path="url(#back-clip)">
      <rect class="card-paper" width="400" height="700"/>
      <rect class="truck-photo" width="400" height="300" fill="url(#photo-tones)"
            role="img" aria-label="Photo of a logging truck driving through a pine forest"/>
      <path d="M0,150 C70,300 330,300 400,150 V700 H0 Z" fill="var(--navy)"/>
      <path class="arc-rule" d="M0,150 C70,300 330,300 400,150"/>
      <path class="card-paper" d="M0,650 C50,470 350,470 400,650 V700 H0 Z"/>
      <path class="arc-rule" d="M0,650 C50,470 350,470 400,650"/>

      <text class="back-brand" x="200" y="322" font-size="26" text-anchor="middle">Hallowell &amp; Hallowell</text>
      <text class="person-name" x="200" y="378" font-size="21" text-anchor="middle">DEAN HALLOWELL</text>
      <text class="person-role" x="200" y="410" font-size="17" text-anchor="middle">Owner | Manager | Maintenance</text>
      <g class="contact-row" transform="translate(112 436)">
        <circle class="icon-light" cx="8" cy="0" r="8"/>
        <path d="M4.5,-3.5 l2,-1 1.5,2.5 -1.5,1 a5,5 0 0 0 2.5,2.5 l1,-1.5 2.5,1.5 -1,2 a8,8 0 0 1 -7,-7 z" fill="var(--navy)"/>
        <text class="contact-light" x="24" y="7" font-size="19">903-512-4097</text>
      </g>

      <g class="contact-row" transform="translate(80 560)">
        <path class="icon-dark" d="M7,-12 a7,7 0 0 1 7,7 c0,6 -7,13 -7,13 c0,0 -7,-7 -7,-13 a7,7 0 0 1 7,-7 z M7,-8 a3,3 0 1 0 0.01,0 z"/>
        <text class="contact-dark" x="22" y="4" font-size="18">4718 Juniper Ln., Larkfield</text>
      </g>
      <text class="contact-dark" x="200" y="590" font-size="18" text-anchor="middle">Ohio 75392</text>
      <g class="contact-row" transform="translate(124 622)">
        <circle class="icon-dark" cx="8" cy="-6" r="8"/>
        <path d="M4.5,-9.5 l2,-1 1.5,2.5 -1.5,1 a5,5 0 0 0 2.5,2.5 l1,-1.5 2.5,1.5 -1,2 a8,8 0 0 1 -7,-7 z" fill="#ffffff"/>
        <text class="contact-dark" x="24" y="0" font-size="18">903-659-3021</text>
      </g>
    </g>
  </g>
</svg>
</body>
</html>
```